New Website for IT Services Business

We need an uncoded web design for a new company based in Australia called "Falcon IT". We offer specialised point of sale (POS) support to the hospitality industry. We already support hundreds of cafes and restaurants. We are also about to launch and promote a range of new services with the offering of General IT Support being the most important. Other additional services to be offered are Falcon Vault Storage, reselling and supporting Corvel Shieldware and Trelmo Suite.

We have a logo design and our colour scheme is based on the logo with the addition of charcoal grey (see attached logos). We want the pages to reflect precision and efficiency with sharp characteristics. It must be professional but playful/fun elements are encouraged.

Our target audience is restaurant and cafe owners who are interested in finding high quality POS and IT support for their business.

The main call to action on the home page should be either 'Let's Meet For Coffee!' or 'Find out more (by completing a form)'. If you are unsure about what the general text should say then you can use 'Lorem Ipsum' where required.

The site must be viewable at different resolutions and on smart phones and tablets.

The website structure will be quite simple. We require:
- one impressive landing page. Visitors will quickly determine our services and that we provide a very high level of service while also offering value for money. Obviously a clear list of links (however/wherever you like) to the other pages.
- Simple pages with a similar layout for the following:
- Services - "POS & IT Support for the Hospitality Industry" being the main one. With complementary services also listed. Another call to action on this page with the option of 'Let's Meet For Coffee' or a "More information/Pricing" form to be completed by the visitor.
- Products - will be a small online storefront for a few simple products.
- About - Business background. 2x Directors with a photo and brief Bio.
- Downloads - A list of free files to download. Includes remote access client software.
- Contact Us - Mailing address, Email addresses and Support phone number.

Please feel free to ask any questions about the design. I will assist as much as possible.

Thank you for viewing. We promise to give constructive feedback to every person who submits a design. Thank you so much.

Target Market(s)

Restaurant and Cafe owners.

Industry/Entity Type

Hospitality

Requirements
Must have
• - Viewable on different resolutions and on smart phones and tablets.
- Clear call to action of EITHER 'Let's Meet For Coffee' or a "More information/Pricing" form to be completed by the visitor.

```html
<!DOCTYPE html>
<html lang="en">
<head>
<meta charset="utf-8">
<title>Falcon IT – POS &amp; IT Support</title>
<link rel="stylesheet" href="https://fonts.googleapis.com/css2?family=Ubuntu:wght@400;500&family=Ubuntu+Condensed&display=swap">
<style>
  :root {
    --red: #d21a2e;
    --red-dark: #b0121f;
    --charcoal: #1c1c1c;
    --charcoal-soft: #2d2d2d;
    --ink: #111111;
    --grey-text: #9a9a9a;
    --page: #efeeec;
    --white: #ffffff;
  }
  * { box-sizing: border-box; margin: 0; padding: 0; }
  html, body { width: 1200px; height: 849px; overflow: hidden; background: var(--page); }
  body { font-family: "Ubuntu", sans-serif; color: var(--ink); }

  .site {
    position: relative; width: 1200px; height: 849px; overflow: hidden;
    background: radial-gradient(ellipse at 55% 35%, #fbfbfa 0%, #f3f2f0 55%, #e9e8e6 100%);
  }

  /* Top bar */
  .callbar { position: absolute; top: 20px; right: 162px; display: flex; align-items: center; gap: 6px; }
  .callbar__icon { width: 18px; height: 24px; }
  .callbar__label { font-size: 11px; color: #333; letter-spacing: 0.2px; margin-right: 6px; }
  .callbar__number { font-family: "Ubuntu Condensed", sans-serif; font-size: 25px; color: var(--red); }
  .topline { position: absolute; left: 422px; top: 59px; width: 616px; border-top: 1px dotted #d6d5d3; }

  /* Headline */
  .headline { position: absolute; right: 162px; top: 100px; text-align: right; font-family: "Ubuntu Condensed", sans-serif; line-height: 1; }
  .headline__row { display: block; white-space: nowrap; }
  .headline__row--first { margin-bottom: 2px; }
  .headline__small { font-size: 20px; }
  .headline__mid { font-size: 31px; }
  .headline__big { font-size: 42px; }
  .headline__huge { font-size: 47px; }
  .is-red { color: var(--red); }
  .is-ink { color: var(--ink); }

  /* Call-to-action cards */
  .cta { position: absolute; top: 230px; height: 139px; border: 3px solid #000;
    background: linear-gradient(#4a4a4a 0%, #1e1e1e 32%, #141414 100%); color: var(--white); padding: 14px 18px; }
  .cta--coffee { left: 418px; width: 306px; }
  .cta--pricing { left: 731px; width: 307px; }
  .cta__title { font-size: 17px; font-weight: 400; white-space: nowrap; }
  .cta__title em { font-style: normal; color: var(--red); font-size: 32px; }
  .cta__text { font-size: 11px; line-height: 15px; margin-top: 4px; color: #f2f2f2; }
  .cta__link { display: inline-block; margin-top: 12px; font-size: 11px; color: var(--red); text-decoration: underline; margin-left: 2px; }
  .cta-shadow { position: absolute; left: 440px; top: 369px; width: 600px; height: 14px;
    background: radial-gradient(ellipse at 50% 0%, rgba(0,0,0,0.18), rgba(0,0,0,0) 70%); }

  /* Feature photo */
  .feature { position: absolute; left: 160px; top: 395px; width: 878px; height: 261px; background: var(--white); border: 1px solid #d8d8d8; }
  .feature__photo { position: absolute; left: 5px; top: 5px; width: 868px; height: 250px;
    background: linear-gradient(100deg, #e9c04a 0%, #c9a25a 30%, #d14a3c 52%, #c8a473 70%, #e7dccd 100%); }
  .feature__caption { position: absolute; left: 5px; top: 207px; width: 868px; height: 48px;
    background: linear-gradient(90deg, rgba(255,255,255,0.97) 0%, rgba(255,255,255,0.95) 55%, rgba(255,255,255,0) 78%);
    border-bottom: 2px solid #222; padding: 8px 0 0 15px; font-family: "Ubuntu Condensed", sans-serif; color: var(--red); white-space: nowrap; }
  .feature__caption small { font-size: 16px; }
  .feature__caption strong { font-weight: 400; font-size: 24px; }

  /* Navigation */
  .mainnav { position: absolute; left: 159px; top: 706px; display: flex; align-items: center; height: 35px; }
  .mainnav__item { font-size: 13px; color: #222; text-decoration: none; padding: 0 20px; position: relative; line-height: 35px; }
  .mainnav__item + .mainnav__item::before { content: ""; position: absolute; left: 0; top: 7px; height: 21px; border-left: 1px solid #cfcfcf; }
  .mainnav__item--active { background: var(--red); color: var(--white); padding: 0 12px; }
  .mainnav__item--active + .mainnav__item::before { left: 8px; }
  .mainnav__item--active + .mainnav__item { padding-left: 26px; }

  /* Brand */
  .brand { position: absolute; left: 746px; top: 681px; width: 292px; height: 84px; display: flex; align-items: center; gap: 12px; }
  .brand__dot { width: 78px; height: 78px; border-radius: 50%; background: var(--red); flex: none; }
  .brand__name { font-family: "Ubuntu Condensed", sans-serif; font-size: 54px; color: var(--charcoal); white-space: nowrap; }

  /* Footer */
  .footer-band { position: absolute; left: 0; top: 785px; width: 1200px; height: 7px; background: var(--red); }
  .footer { position: absolute; left: 0; top: 792px; width: 1200px; height: 57px; background: var(--charcoal-soft); }
  .social { position: absolute; left: 160px; top: 18px; display: flex; gap: 10px; }
  .social__dot { width: 14px; height: 14px; border-radius: 50%; background: #7a7a7a; }
  .copyright { position: absolute; right: 162px; top: 19px; font-size: 11px; color: var(--grey-text); letter-spacing: 0.2px; }
</style>
</head>
<body>
<div class="site">

  <div class="callbar">
    <svg class="callbar__icon" viewBox="0 0 18 24" aria-hidden="true">
      <path d="M4 1 L8 1 L8 7 L6 9 Q6 14 9 17 L11 15 L16 19 L15 22 Q12 24 8 21 Q2 15 2 6 Q2 2 4 1 Z" fill="#777"/>
    </svg>
    <span class="callbar__label">CALL US TODAY:</span>
    <span class="callbar__number">0800 -2400 - 300</span>
  </div>
  <div class="topline"></div>

  <h1 class="headline">
    <span class="headline__row headline__row--first">
      <span class="headline__small is-ink">PROVIDE</span>
      <span class="headline__mid is-red">HIGH QUALITY</span>
      <span class="headline__big is-ink">POS &amp; IT</span>
    </span>
    <span class="headline__row">
      <span class="headline__small is-red">SUPPORT FOR</span>
      <span class="headline__huge is-ink">YOUR</span>
      <span class="headline__huge is-red">BUSINESS</span>
    </span>
  </h1>

  <section class="cta cta--coffee">
    <h2 class="cta__title">Let’s Meet For <em>Coffee!</em></h2>
    <p class="cta__text">Lorem ipsum dolor sit amet, consectetuer adipiscing elit, sed diam nonummy nibh euismod tincidunt...</p>
    <a class="cta__link" href="#">READ MORE...</a>
  </section>
  <section class="cta cta--pricing">
    <h2 class="cta__title">More Information / <em>Pricing</em></h2>
    <p class="cta__text">Lorem ipsum dolor sit amet, consectetuer adipiscing elit, sed diam nonummy nibh euismod tincidunt...</p>
    <a class="cta__link" href="#">READ MORE...</a>
  </section>
  <div class="cta-shadow"></div>

  <figure class="feature">
    <div class="feature__photo" role="img" aria-label="Photo of a bright cafe interior with red booths, wooden tables and a smiling staff member"></div>
    <figcaption class="feature__caption"><small>PROVIDE SUPPORT HUNDREDS OF</small> <strong>CAFES &amp; RESTURANTS</strong></figcaption>
  </figure>

  <nav class="mainnav">
    <a class="mainnav__item mainnav__item--active" href="#">Home</a>
    <a class="mainnav__item" href="#">About Us</a>
    <a class="mainnav__item" href="#">Services</a>
    <a class="mainnav__item" href="#">Products</a>
    <a class="mainnav__item" href="#">Download</a>
    <a class="mainnav__item" href="#">Contact</a>
  </nav>

  <div class="brand">
    <span class="brand__dot"></span>
    <span class="brand__name">Falcon IT</span>
  </div>

  <div class="footer-band"></div>
  <footer class="footer">
    <div class="social">
      <span class="social__dot"></span>
      <span class="social__dot"></span>
      <span class="social__dot"></span>
      <span class="social__dot"></span>
      <span class="social__dot"></span>
    </div>
    <p class="copyright">© 2012 Falcon IT. All rights reserved.</p>
  </footer>

</div>
</body>
</html>
```